Gymnastics Award Design Needed--for kids

Need a gymnastics certificate or award designed. Will be printed on a piece of 8.5x11 paper. The award will be celebrating the gymnast learning a new skill in gymnastics. So it should be fun, but still look "official". Needs to look good hanging on a gymnast's bedroom wall.

It should say "The Soaring Handspring Club"
I will be using this design to change it based on the skill.

My main colors are:
#34475D
#E1467A
#7555A4

So should use those, but can add others

My website is tumblenestpro.com so you can see the look/feel.

Target Market(s)

Main audience will be girls ages 5-12, but will also be used by slightly older girls and boys. So needs to be fun, not too gender specific.

Industry/Entity Type

Learning

Requirements
Must have
• The following will need to go on the certificate:
• * Name of Skill
• * Image of Skill
• * Gymnast's Name
• * my logo
• * Gym's Logo
• * Gym's Name
• Optional: Date

```html
<!DOCTYPE html>
<html lang="en">
<head>
<meta charset="utf-8">
<title>The Soaring Handspring Club – Certificate of Attendance</title>
<link rel="stylesheet" href="https://fonts.googleapis.com/css2?family=Alfa+Slab+One&family=Dancing+Script:wght@600&family=Lobster&family=Open+Sans:wght@400;600&family=Rubik:wght@800&display=swap">
<style>
  :root {
    --backdrop: #2c0a47;
    --paper: #f4f0ec;
    --purple: #7555a4;
    --pink: #e1467a;
    --crimson: #c8215a;
    --ink: #1e1e1e;
    --navy: #2343a0;
    --rosette: #f1b9cf;
    --fine-line: #c9b3e0;
  }
  * { margin: 0; padding: 0; box-sizing: border-box; }
  html, body { width: 800px; height: 1200px; overflow: hidden; }
  body { background: var(--backdrop); position: relative; font-family: "Open Sans", sans-serif; }

  .certificate {
    position: absolute; left: 30px; top: 314px;
    width: 740px; height: 572px;
    background: var(--paper);
    box-shadow: 0 10px 30px rgba(0,0,0,.45);
  }
  .frame { position: absolute; inset: 0; }

  .club-title { position: absolute; left: 0; top: 0; width: 740px; height: 160px; }
  .club-title text { font-family: "Rubik", sans-serif; font-weight: 800; font-size: 30px; fill: var(--purple); letter-spacing: 1px; }

  .skill-art {
    position: absolute; left: 264px; top: 142px; width: 212px; height: 66px;
    background: linear-gradient(90deg, #f3d7cb, #e98a9e 50%, #f3d7cb);
    border-bottom: 2px solid #c9b9a8;
  }

  .centered { position: absolute; left: 0; width: 740px; text-align: center; }
  .award-type { top: 220px; font-family: "Lobster", "Yellowtail", cursive; font-weight: 400; font-size: 38px; color: var(--crimson); line-height: 1.1; }
  .presented { top: 274px; font-size: 15px; color: var(--ink); }
  .recipient { top: 298px; font-family: "Alfa Slab One", serif; font-size: 28px; letter-spacing: 1px; color: var(--ink); line-height: 1.1; }
  .name-rule { position: absolute; left: 178px; top: 337px; width: 384px; border-top: 1.5px solid var(--ink); }
  .citation { top: 346px; font-size: 15px; line-height: 22px; color: var(--ink); }

  .gym-signature {
    position: absolute; left: 124px; top: 405px; width: 166px;
    font-family: "Dancing Script", cursive; font-weight: 600; font-size: 20px; color: var(--ink);
    text-align: center; border-bottom: 1.5px solid var(--ink); line-height: 28px;
  }
  .gym-name {
    position: absolute; left: 133px; top: 442px;
    display: flex; align-items: center; gap: 6px;
    font-size: 15px; font-weight: 600; color: var(--navy);
  }
  .gym-name .mark { width: 12px; height: 12px; background: var(--navy); }

  .brand-name {
    position: absolute; left: 362px; top: 420px;
    display: flex; align-items: center; gap: 10px;
    font-size: 26px; font-weight: 400; color: var(--pink); letter-spacing: 1px;
  }
  .brand-name .mark { width: 22px; height: 22px; border-radius: 50%; background: var(--purple); }
</style>
</head>
<body>
  <main class="certificate">
    <svg class="frame" width="740" height="572" viewBox="0 0 740 572" aria-hidden="true">
      <rect x="76" y="26" width="588" height="12" fill="var(--purple)"/>
      <rect x="76" y="38" width="588" height="12" fill="var(--pink)"/>
      <rect x="76" y="516" width="588" height="14" fill="var(--pink)"/>
      <rect x="76" y="530" width="588" height="13" fill="var(--purple)"/>
      <rect x="27" y="72" width="13" height="426" fill="var(--purple)"/>
      <rect x="40" y="72" width="14" height="426" fill="var(--pink)"/>
      <rect x="686" y="72" width="14" height="426" fill="var(--pink)"/>
      <rect x="700" y="72" width="13" height="426" fill="var(--purple)"/>
    </svg>
    <svg class="frame" width="740" height="572" viewBox="0 0 740 572">
      <g role="img" aria-label="Corner rosette ornaments">
        <circle cx="46" cy="44" r="27" fill="var(--rosette)"/>
        <circle cx="694" cy="44" r="27" fill="var(--rosette)"/>
        <circle cx="46" cy="527" r="27" fill="var(--rosette)"/>
        <circle cx="694" cy="527" r="27" fill="var(--rosette)"/>
      </g>
    </svg>

    <svg class="club-title" viewBox="0 0 740 160">
      <defs><path id="title-arc" d="M100 155 Q370 62 640 155"/></defs>
      <text text-anchor="middle"><textPath href="#title-arc" startOffset="50%">The SOARING HANDSPRING CLUB</textPath></text>
    </svg>

    <div class="skill-art" role="img" aria-label="Illustration of a gymnast performing the stages of a handspring"></div>

    <h1 class="centered award-type">Certificate of Attendance</h1>
    <p class="centered presented">Presented to</p>
    <p class="centered recipient">LILY CARTER</p>
    <div class="name-rule"></div>
    <p class="centered citation">for successfully attending Gymnastics Classes at<br>Maple Ridge Gymnastics Gym from January 1 to February 17, 2017.</p>

    <p class="gym-signature">Maple Ridge Gym</p>
    <p class="gym-name"><span class="mark"></span>Maple Ridge Gym</p>

    <p class="brand-name"><span class="mark"></span>TumbleNest Pro</p>
  </main>
</body>
</html>
```